label design for our sauces - please note not a flyer - but a LABEL for a jam & sauce jar
I have attached a sample of a few done by a friend. They are ok but I want something more please.
I am looking for it to be a bit sharper, font like the logo and some separation of the areas on the sides of the labels. Lines or dots or something.
I do also want to consider adding a piece of fruit as either a nice image or a stock line drawing. Id like a few options please? we have in total 12 labels we need asap and then we will want about another 12 after that.
See our competitors that we are trying to take inspiration from.
https://www.tallowmire.com.au - see particularly their strawberry jam label
also see https://www.kevin.com.au as a smaple of a nice whaite label but We want the trees to be a color as well as the top and bottom band.
Also we want 2 ranges, one with the white label and color on the band and the tree but the rest black text and then a black label with white text and a gold bad and leaves on the tree.
Can you please take these guides and create something please. the size of the labels to print is 60x160
Id like to get something in the next 24 hours if possible as I really need to get this completed this week.....

```html
<!DOCTYPE html>
<html lang="en">
<head>
<meta charset="utf-8">
<title>Fenwick's Larder – Pineapple Rum Jam Label</title>
<link rel="stylesheet" href="https://fonts.googleapis.com/css2?family=Oswald:wght@500;600&family=Cinzel:wght@400&family=Lato:wght@400;700&family=Libre+Baskerville&display=swap">
<style>
  :root {
    --canvas-bg: #e6e6e6;
    --label-black: #050505;
    --frame-line: #d9d9d9;
    --gold: #f4b521;
    --band-orange: #ffb347;
    --band-pale: #fff1b8;
    --band-mid: #f9d98a;
    --white: #ffffff;
  }
  html, body {
    margin: 0;
    padding: 0;
    width: 1200px;
    height: 1200px;
    overflow: hidden;
    background: var(--canvas-bg);
  }
  .canvas {
    position: relative;
    width: 1200px;
    height: 1200px;
  }
  .side-band {
    position: absolute;
    left: 100px;
    top: 390px;
    width: 1000px;
    height: 460px;
    background: var(--band-orange);
  }
  .side-band__pattern {
    position: absolute;
    left: 0;
    right: 0;
    top: 26px;
    bottom: 26px;
    background: linear-gradient(90deg, var(--band-pale), var(--band-mid) 30%, var(--band-pale) 50%, var(--band-mid) 70%, var(--band-pale));
  }
  .front-panel {
    position: absolute;
    left: 320px;
    top: 290px;
    width: 560px;
    height: 660px;
    background: var(--label-black);
    clip-path: polygon(26px 0, calc(100% - 26px) 0, 100% 26px, 100% calc(100% - 26px), calc(100% - 26px) 100%, 26px 100%, 0 calc(100% - 26px), 0 26px);
  }
  .front-panel__frame {
    position: absolute;
    inset: 0;
  }
  .front-panel__content {
    position: absolute;
    inset: 0;
    display: flex;
    flex-direction: column;
    align-items: center;
    text-align: center;
    color: var(--white);
  }
  .brand {
    margin-top: 110px;
    display: flex;
    align-items: center;
    gap: 12px;
  }
  .brand__dot {
    width: 14px;
    height: 14px;
    border-radius: 50%;
    background: var(--gold);
  }
  .brand__name {
    font-family: 'Oswald', sans-serif;
    font-weight: 500;
    font-size: 40px;
    letter-spacing: 0.5px;
    color: var(--white);
  }
  .brand__tagline {
    margin-top: 4px;
    font-family: 'Lato', sans-serif;
    font-size: 13px;
    letter-spacing: 2px;
    color: var(--white);
  }
  .product-name {
    margin-top: 30px;
    font-family: 'Cinzel', serif;
    font-weight: 400;
    font-size: 50px;
    line-height: 62px;
    letter-spacing: 4px;
    color: var(--gold);
  }
  .ingredients-note {
    margin-top: 30px;
    font-family: 'Libre Baskerville', serif;
    font-size: 18px;
    color: var(--white);
  }
  .dietary-claim {
    margin-top: 2px;
    font-family: 'Oswald', sans-serif;
    font-weight: 600;
    font-size: 54px;
    letter-spacing: 1px;
    line-height: 1.1;
  }
  .net-weight {
    margin-top: 22px;
    font-family: 'Lato', sans-serif;
    font-weight: 700;
    font-size: 26px;
    letter-spacing: 1px;
  }
</style>
</head>
<body>
<main class="canvas">
  <div class="side-band">
    <div class="side-band__pattern" role="img" aria-label="Pale golden pineapple skin and leaf pattern"></div>
  </div>

  <section class="front-panel">
    <svg class="front-panel__frame" width="560" height="660" viewBox="0 0 560 660" aria-hidden="true">
      <polygon points="30,10 530,10 550,30 550,630 530,650 30,650 10,630 10,30"
               fill="none" stroke="var(--frame-line)" stroke-width="1.5"/>
    </svg>
    <div class="front-panel__content">
      <div class="brand">
        <span class="brand__dot"></span>
        <span class="brand__name">FENWICK'S LARDER</span>
      </div>
      <div class="brand__tagline">PROUDLY AUSTRALIAN SINCE 1987</div>
      <h1 class="product-name" style="margin-bottom:0;">PINEAPPLE<br>RUM JAM</h1>
      <p class="ingredients-note" style="margin-bottom:0;">All Natural Ingredients</p>
      <div class="dietary-claim">GLUTEN FREE</div>
      <div class="net-weight">215 gm</div>
    </div>
  </section>
</main>
</body>
</html>
```